Mortgage Lender needs Flyers Designed

We are a wholesale mortgage lender providing mortgage services throughout the United States to mortgage brokers. We just merged with a company and need to redesign their product flyers and matrices so they are more in line with a modern and sleek look. We provide residential and commercial mortgage financing options. I have attached a document labeled FULL STACK. This is the current flyer set that needs to be redesigned for my company. There are 10 programs featured in the document. The first two pages provide a product overview and the following 17 pages are the matrices for each product. I need a design set created in either Adobe Photoshop or Adobe Indesign so we can edit the content as necessary.

Target Market(s)

Mortgage Brokers in the United States

Industry/Entity Type

Finance, Mortgage

Font styles to use
Serif
Sans Serif

Requirements
Must have
• Must include all ten programs and must be designed using Adobe Photoshop or Adobe InDesign (preferred)
Nice to have
• Great graphics and clean modern feel.
Should not have
• Typos, hard to edit fields, should not look very similar to the FULL STACK pdf attached.

```html
<!DOCTYPE html>
<html lang="en">
<head>
<meta charset="utf-8">
<title>Northvale Lending – Product Overview &amp; Program Matrix</title>
<link href="https://fonts.googleapis.com/css2?family=Merriweather:wght@700;900&family=Open+Sans:ital,wght@0,300;0,400;0,600;0,700;1,400&family=Roboto+Condensed:wght@400;500;700&display=swap" rel="stylesheet">
<style>
:root{
  --backdrop:#d9d9d9;
  --charcoal:#202020;
  --green-deep:#1b3619;
  --green-photo:#2f5a2a;
  --lime:#a6f39b;
  --ink:#1d1d1d;
  --muted:#555;
  --panel-gray:#a4a4a4;
  --cell-gray:#9d9d9d;
  --rule:#c8c8c8;
  --white:#fff;
}
*{box-sizing:border-box}
html,body{margin:0;padding:0}
body{width:1200px;height:2268px;overflow:hidden;background:var(--backdrop);position:relative;font-family:'Open Sans',sans-serif;color:var(--ink)}
.page{position:absolute;width:555px;height:718px;overflow:hidden;box-shadow:3px 4px 9px rgba(0,0,0,.35)}
.page--dark{background:var(--charcoal)}
.page--light{background:var(--white)}

/* ---------- cover ---------- */
.cover-photo{position:absolute;left:0;top:0;width:555px;height:433px;background:linear-gradient(135deg,#365f30 0%,#2a4d26 45%,#1e3a1b 100%)}
.cover-shapes{position:absolute;left:0;top:0}
.brand{position:absolute;left:22px;top:58px;display:flex;align-items:center;gap:6px}
.brand__mark{width:10px;height:10px;background:var(--green-deep)}
.brand__name{font-family:'Open Sans',sans-serif;font-weight:700;font-size:10.5px;color:var(--green-deep);letter-spacing:.3px}
.cover-title{position:absolute;left:38px;top:365px;color:var(--white);font-family:'Merriweather',serif;font-weight:900;line-height:1}
.cover-title__kicker{font-size:19px;letter-spacing:2px}
.cover-title__main{font-size:38px;margin-top:3px}

.ribbon-tag{position:absolute}
.ribbon-tag svg{position:absolute;left:0;top:0;width:100%;height:100%}
.ribbon-tag span{position:relative;display:block;padding-left:11px;font-family:'Merriweather',serif;font-weight:900;color:var(--lime);white-space:nowrap}

.program-label{position:absolute;font-family:'Roboto Condensed',sans-serif;font-weight:500;color:var(--white);font-size:11.5px;letter-spacing:.4px;line-height:1.15;text-transform:uppercase}
.badge-new{display:inline-block;background:var(--lime);color:var(--green-deep);font-weight:700;padding:0 4px;margin-left:4px;border-radius:2px}

.program-card{position:absolute;background:var(--white);border-radius:5px;overflow:hidden;width:158px}
.program-card__head{background:var(--lime);color:var(--ink);font-size:7.4px;padding:4px 8px;line-height:1.55}
.program-card__head b{font-weight:400}
.program-card__list{list-style:none;margin:0;padding:5px 6px 4px 8px}
.program-card__list li{position:relative;padding-left:10px;font-size:7.3px;line-height:1.42;color:var(--muted);margin-bottom:1.5px}
.program-card__list li::before{content:'';position:absolute;left:0;top:2.6px;width:5px;height:5px;border:1px solid #666;border-radius:50%}
.program-card__list li::after{content:'';position:absolute;left:2.3px;top:3.3px;width:1.4px;height:2.6px;border:solid #666;border-width:0 1px 1px 0;transform:rotate(45deg)}

/* ---------- matrix pages ---------- */
.matrix-header{position:absolute;left:0;top:0;width:555px;height:51px;background:var(--charcoal)}
.matrix-header svg{position:absolute;left:0;top:0}
.matrix-header__title{position:absolute;left:43px;top:16px;font-family:'Merriweather',serif;font-weight:900;font-size:16.5px;color:var(--white)}
.matrix-header__sub{position:absolute;right:42px;top:20px;font-size:11.5px;font-weight:300;color:#e6e6e6}

.table-title{position:absolute;font-size:6.8px;line-height:1.35;color:var(--ink)}
.table-title strong{font-weight:600;text-transform:uppercase}
.table-title.plain strong{text-transform:none}

.matrix{position:absolute;border-collapse:collapse;table-layout:fixed;border:.6px solid #bdbdbd}
.matrix th{background:var(--green-deep);color:var(--white);font-size:5.3px;font-weight:600;line-height:1.15;padding:1.5px 1px;text-align:center;border-right:.6px solid #456}
.matrix td{font-size:5.5px;text-align:center;border-bottom:.6px solid var(--rule);border-right:.6px solid var(--rule);height:12px;padding:0 1px}
.matrix td.na{background:var(--cell-gray)}
.note{position:absolute;font-size:5px;font-style:italic;color:#444;line-height:1.3}

.section-tag{position:absolute;height:25px;background:var(--green-deep);clip-path:polygon(0 0,86% 0,100% 100%,0 100%);color:var(--white);font-family:'Merriweather',serif;font-weight:900;font-size:8.6px;line-height:25px;padding-left:11px;letter-spacing:.5px;text-transform:uppercase;white-space:nowrap}

.spec-table{position:absolute;border-collapse:collapse;table-layout:fixed}
.spec-table td{font-size:5.4px;line-height:1.35;vertical-align:top;padding:2.2px 4px}
.spec-table td.label{background:var(--charcoal);color:var(--white);font-weight:600}
.spec-table td.value{background:var(--panel-gray);color:#1c1c1c}
.spec-table td.value b{font-weight:700}

.bullet-notes{position:absolute;list-style:none;margin:0;padding:0}
.bullet-notes li{position:relative;padding-left:8px;font-size:5.4px;line-height:1.35;color:#444;margin-bottom:3px}
.bullet-notes li::before{content:'';position:absolute;left:0;top:1.5px;width:4px;height:4px;border:.8px solid #666;border-radius:50%}

.plain-list{position:absolute;font-size:5.5px;line-height:1.45;color:#222}
.plain-list div{display:flex}
.plain-list span:first-child{display:inline-block}

.page-footer{position:absolute;left:43px;right:43px;top:690px;display:flex;align-items:center;gap:6px;font-size:4.8px;color:#333}
.page-footer i{font-style:italic}
.page-footer__rule{flex:1;height:.6px;background:#999}
.page-footer__num{font-weight:700}
</style>
</head>
<body>

<!-- ===================== PAGE 1 : COVER ===================== -->
<section class="page page--dark" style="left:33px;top:35px">
  <div class="cover-photo" role="img" aria-label="Photo of a couple reviewing house plans at a table, tinted green"></div>
  <svg class="cover-shapes" width="555" height="460" viewBox="0 0 555 460" aria-hidden="true">
    <polygon points="0,0 200,0 0,180" fill="#ffffff"/>
    <polygon points="200,0 216,0 0,195 0,180" fill="#a6f39b"/>
    <polygon points="0,195 128,80 355,433 0,433" fill="#1b3619"/>
    <polygon points="40,434 545,434 532,443 26,443" fill="#a6f39b"/>
  </svg>
  <div class="brand"><span class="brand__mark"></span><span class="brand__name">NORTHVALE LENDING</span></div>
  <div class="cover-title">
    <div class="cover-title__kicker">PRODUCT</div>
    <div class="cover-title__main">Overview</div>
  </div>

  <div class="ribbon-tag" style="left:32px;top:459px;width:323px;height:26px">
    <svg viewBox="0 0 323 26" preserveAspectRatio="none"><polygon points="0.5,0.5 300,0.5 322.5,25.5 0.5,25.5" fill="#1b3619" stroke="#a6f39b" stroke-width="1"/></svg>
    <span style="font-size:15.5px;line-height:26px">For Investments or Consumers</span>
  </div>
  <div class="program-label" style="left:43px;top:499px;font-size:12px">Summit Select <span class="badge-new">NEW!</span></div>

  <div class="program-card" style="left:32px;top:526px;height:167px">
    <div class="program-card__head"><b>Primary &amp; Second Home</b><br>FICO 620+ / 90 CLTV Max / $3.5MM</div>
    <ul class="program-card__list">
      <li>Primary purchase to $3.5MM</li>
      <li>Purchase &amp; R/T to $3.0MM, 90 LTV</li>
      <li>Cash out to $3.0MM, 85 LTV</li>
      <li>55% DTI up to 80 LTV; 680+ FICO</li>
      <li>Asset depletion available</li>
      <li>Foreign National second home eligible</li>
      <li>Single family, 2-4 unit, condo, nonwarrantable condo, condotel, rural</li>
    </ul>
  </div>
  <div class="program-card" style="left:197px;top:526px;height:167px">
    <div class="program-card__head"><b>Investment - Income Qualifying</b><br>FICO 620+ / 80 CLTV Max / $3.0MM</div>
    <ul class="program-card__list">
      <li>Full &amp; alternative document options</li>
      <li>Purchase &amp; R/T up to $3.0MM, 80 LTV</li>
      <li>Cash out up to $3.0MM, 75 LTV</li>
      <li>Asset depletion available</li>
      <li>Foreign National eligible</li>
      <li>Single family, 2-4 unit, condo, nonwarrantable condo, condotel, rural</li>
    </ul>
  </div>
  <div class="program-card" style="left:364px;top:526px;height:167px">
    <div class="program-card__head"><b>Investment - DSCR</b><br>FICO 640+ / 80 CLTV Max / $2.0MM</div>
    <ul class="program-card__list">
      <li>DSCR ≥ .75</li>
      <li>Purchase &amp; R/T up to $2.0MM, 80 LTV</li>
      <li>Cash out up to $2.0MM, 75 LTV</li>
      <li>Short term rental refinance up to $2.0MM</li>
      <li>Foreign National eligible</li>
      <li>Single family, 2-4 unit, condo, nonwarrantable condo, condotel, rural</li>
    </ul>
  </div>
</section>

<!-- ===================== PAGE 2 : PROGRAM OVERVIEW ===================== -->
<section class="page page--dark" style="left:606px;top:35px">
  <div class="ribbon-tag" style="left:31px;top:29px;width:194px;height:26px">
    <svg viewBox="0 0 194 26" preserveAspectRatio="none"><polygon points="0.5,0.5 175,0.5 193.5,25.5 0.5,25.5" fill="#1b3619" stroke="#a6f39b" stroke-width="1"/></svg>
    <span style="font-size:15.5px;line-height:26px">For Investments</span>
  </div>

  <div class="program-label" style="left:45px;top:64px">Keystone Investor</div>
  <div class="program-label" style="left:203px;top:64px">Portfolio Pro</div>
  <div class="program-label" style="left:369px;top:64px">Rent Yield Plus</div>

  <div class="program-card" style="left:32px;top:85px;height:158px">
    <div class="program-card__head">FICO 620+ / 80 CLTV Max / $3MM</div>
    <ul class="program-card__list">
      <li>Non-owner occupied business purpose loans</li>
      <li>DSCR ≥ .75</li>
      <li>Income qualifying option</li>
      <li>Interest only option</li>
      <li>Purchase up to $3MM</li>
      <li>Cash out up to 75 CLTV</li>
      <li>Foreign National eligible</li>
      <li>Condo, non-warrantable condo, 2-4 unit, modular</li>
    </ul>
  </div>
  <div class="program-card" style="left:197px;top:85px;height:158px">
    <div class="program-card__head">FICO 660+ / 75 CLTV Max / $3MM</div>
    <ul class="program-card__list">
      <li>DSCR non-owner occupied business purpose loans</li>
      <li>DSCR ≥ 1.0</li>
      <li>Interest only option</li>
      <li>Purchase up to $3MM</li>
      <li>Cash out up to 65 CLTV</li>
      <li>5-8 units</li>
      <li>Mixed-Use 2-8 units</li>
      <li>Cross-collateralized blanket loans up to 25 properties</li>
    </ul>
  </div>
  <div class="program-card" style="left:364px;top:85px;height:158px">
    <div class="program-card__head">FICO 700+ / 80 CLTV Max / $2MM</div>
    <ul class="program-card__list">
      <li>DSCR ≥ 1.0</li>
      <li>Purchase up to $2MM</li>
      <li>Cash out up to 75 CLTV</li>
      <li>Interest only option</li>
      <li>Reserves as low as 3 months</li>
      <li>Single family, condo, 2-4 unit</li>
    </ul>
  </div>

  <div class="ribbon-tag" style="left:31px;top:270px;width:194px;height:26px">
    <svg viewBox="0 0 194 26" preserveAspectRatio="none"><polygon points="0.5,0.5 175,0.5 193.5,25.5 0.5,25.5" fill="#1b3619" stroke="#a6f39b" stroke-width="1"/></svg>
    <span style="font-size:15.5px;line-height:26px">For Consumers</span>
  </div>

  <div class="program-label" style="left:42px;top:311px">Open Path</div>
  <div class="program-label" style="left:205px;top:311px">Granite Prime</div>
  <div class="program-label" style="left:369px;top:311px">Equity Key</div>

  <div class="program-card" style="left:32px;top:332px;height:154px">
    <div class="program-card__head">FICO 620+ / 90 CLTV Max / $4MM</div>
    <ul class="program-card__list">
      <li>Owner occupied: Primary &amp; 2nd</li>
      <li>Fixed terms: 15, 30, 40-Yr (IO)</li>
      <li>Purchase up to $4MM</li>
      <li>Cash out up to 80 CLTV</li>
      <li>Full &amp; alternative document</li>
      <li>Asset depletion available</li>
      <li>Foreign National 2nd home</li>
      <li>Single family, condo, nonwarrantable condo, 2-4 unit, modular, rural</li>
    </ul>
  </div>
  <div class="program-card" style="left:197px;top:332px;height:154px">
    <div class="program-card__head">FICO 700+ / 90 CLTV Max / $2.5MM</div>
    <ul class="program-card__list">
      <li>Owner occupied: Primary &amp; 2nd</li>
      <li>Fixed terms: 15, 30, 40-Yr (IO)</li>
      <li>Purchase up to $2.5MM</li>
      <li>Cash out up to 80 CLTV</li>
      <li>Property up to 20 acres</li>
      <li>Single family, 2-unit, condo, nonwarrantable condo, rural</li>
    </ul>
  </div>
  <div class="program-card" style="left:364px;top:332px;height:154px">
    <div class="program-card__head">FICO 680+ / 90 CLTV Max / $500k</div>
    <ul class="program-card__list">
      <li>2nd liens: closed end, HELOC</li>
      <li>Owner &amp; non-owner occupied</li>
      <li>Fixed terms: 10, 15, 20, 30 year</li>
      <li>Balloon options: 30/15, 40/15</li>
      <li>Loan amounts up to $500k</li>
      <li>Combined lien up to $2.5MM</li>
      <li>Full &amp; alternative document</li>
      <li>Single family, condo, 2-4 units</li>
      <li>Bank Statement HELOC option</li>
    </ul>
  </div>

  <div class="program-label" style="left:42px;top:517px">Jumbo Elite</div>
  <div class="program-label" style="left:205px;top:501px">Jumbo Elite<br>Fixed Plus</div>
  <div class="program-label" style="left:369px;top:517px">QM Jumbo Core</div>

  <div class="program-card" style="left:32px;top:537px;height:147px">
    <div class="program-card__head">FICO 700+ / 80 CLTV Max / $3MM</div>
    <ul class="program-card__list">
      <li>Owner occupied: Primary</li>
      <li>5/6, 7/6, 10/6, 15-Yr Fixed</li>
      <li>Purchase up to $3MM</li>
      <li>Cash out up to 65 CLTV</li>
      <li>Single family, PUD, warrantable condo, townhouse</li>
    </ul>
  </div>
  <div class="program-card" style="left:197px;top:537px;height:147px">
    <div class="program-card__head">FICO 700+ / 80 CLTV Max / $3.5MM</div>
    <ul class="program-card__list">
      <li>Owner occupied: Primary &amp; 2nd</li>
      <li>Fixed terms: 30, 40-Yr</li>
      <li>Interest only: 30/10, 40/10</li>
      <li>Purchase up to $3.5MM</li>
      <li>Cash out up to 80 CLTV</li>
      <li>Full Documentation 12, 24 months</li>
      <li>Single family, PUD, 2-unit, warrantable condo</li>
    </ul>
  </div>
  <div class="program-card" style="left:364px;top:537px;height:147px">
    <div class="program-card__head">FICO 680+ / 89.99 CLTV Max / $2.5MM</div>
    <ul class="program-card__list">
      <li>Owner &amp; non-owner occupied</li>
      <li>30-Yr Fixed</li>
      <li>$750k max cash-in-hand</li>
      <li>Loan amounts up to $2.5MM</li>
      <li>FTHB up to $1.5MM</li>
      <li>Single family, warrantable condo, 1-4 unit Investment</li>
      <li>AUS findings required</li>
    </ul>
  </div>
</section>

<!-- ===================== PAGE 3 : SUMMIT SELECT MATRIX 1 ===================== -->
<section class="page page--light" style="left:33px;top:772px">
  <header class="matrix-header">
    <svg width="300" height="51" viewBox="0 0 300 51" aria-hidden="true"><polygon points="0,0 266,0 296,51 0,51" fill="#1b3619"/></svg>
    <div class="matrix-header__title">Summit Select</div>
    <div class="matrix-header__sub">Program Matrix</div>
  </header>

  <div class="table-title" style="left:43px;top:74px"><strong>Primary Residence</strong><br>Full &amp; Alternative Document</div>
  <table class="matrix" style="left:43px;top:98px;width:212px">
    <colgroup><col style="width:23%"><col style="width:27%"><col style="width:25%"><col style="width:25%"></colgroup>
    <tr><th>FICO</th><th>Loan Amount</th><th>Purchase &amp;<br>R/T LTV</th><th>Cash Out<br>LTV</th></tr>
    <tr><td>760</td><td>$3.5MM*</td><td>70</td><td class="na"></td></tr>
    <tr><td>680 - 759</td><td>$3.0MM</td><td>90</td><td>85</td></tr>
    <tr><td>640 - 679</td><td>$3.0MM</td><td>85</td><td>80</td></tr>
    <tr><td>620 - 639</td><td>$2.5MM</td><td>80</td><td>75</td></tr>
  </table>
  <div class="note" style="left:195px;top:170px">*Full Documentation Only</div>

  <div class="table-title" style="left:296px;top:74px"><strong>Second Home</strong><br>Full &amp; Alternative Document</div>
  <table class="matrix" style="left:296px;top:98px;width:212px">
    <colgroup><col style="width:23%"><col style="width:27%"><col style="width:25%"><col style="width:25%"></colgroup>
    <tr><th>FICO</th><th>Loan Amount</th><th>Purchase &amp;<br>R/T LTV</th><th>Cash Out<br>LTV</th></tr>
    <tr><td style="height:16px">680</td><td>$3.0MM</td><td>90</td><td>85</td></tr>
    <tr><td style="height:16px">640 - 679</td><td>$3.0MM</td><td>85</td><td>80</td></tr>
    <tr><td style="height:16px">620 - 639</td><td>$2.5MM</td><td>80</td><td>75</td></tr>
  </table>

  <div class="table-title" style="left:43px;top:202px"><strong>Investment - Income Qualifying</strong><br>Full &amp; Alternative Document</div>
  <table class="matrix" style="left:43px;top:224px;width:212px">
    <colgroup><col style="width:23%"><col style="width:27%"><col style="width:25%"><col style="width:25%"></colgroup>
    <tr><th>FICO</th><th>Loan Amount</th><th>Purchase &amp;<br>R/T LTV</th><th>Cash Out<br>LTV</th></tr>
    <tr><td style="height:16px">680</td><td>$3.0MM</td><td>80</td><td>75</td></tr>
    <tr><td style="height:16px">640 - 679</td><td>$3.0MM</td><td>75</td><td>70</td></tr>
    <tr><td style="height:16px">620 - 639</td><td>$2.5MM</td><td>70</td><td>65</td></tr>
  </table>

  <div class="table-title" style="left:296px;top:212px"><strong>Investment - DSCR</strong></div>
  <table class="matrix" style="left:296px;top:224px;width:212px">
    <colgroup><col style="width:18%"><col style="width:20%"><col style="width:22%"><col style="width:20%"><col style="width:20%"></colgroup>
    <tr><th>FICO</th><th>DSCR Ratio</th><th>Loan Amount<br>R/T LTV</th><th>Purchase &amp;<br>LTV</th><th>Cash Out</th></tr>
    <tr><td>680</td><td rowspan="2">≥ 1.00</td><td>$2.0MM</td><td>80</td><td>75</td></tr>
    <tr><td>640 - 679</td><td>$1.5MM</td><td>75</td><td>70</td></tr>
    <tr><td>680</td><td rowspan="2">.75 - .99</td><td>$1.5MM</td><td>70</td><td>65</td></tr>
    <tr><td>640 - 679</td><td>$1.0MM</td><td>65</td><td>60*</td></tr>
  </table>
  <div class="note" style="left:482px;top:296px">*FICO ≥ 660</div>

  <div class="section-tag" style="left:43px;top:330px;width:175px">General Requirements</div>
  <table class="spec-table" style="left:43px;top:365px;width:241px;height:312px">
    <colgroup><col style="width:26%"><col style="width:74%"></colgroup>
    <tr><td class="label">Exceptions</td><td class="value">Not Permitted</td></tr>
    <tr><td class="label">Product Type</td><td class="value">Fixed Rate: 15, 30, 40 year; ARM: 5/6m, 7/6m, 10/6m</td></tr>
    <tr><td class="label">Interest Only</td><td class="value">Fixed Rate: 30, 40 year term only. Use cash out LTV thresholds for eligibility</td></tr>
    <tr><td class="label">Documentation</td><td class="value">Full Documentation, Bank Statements, Asset Depletion, 1099, P&amp;L + 2 months bank statements (80 LTV max; 50% DTI max), DSCR</td></tr>
    <tr><td class="label">Loan Amount</td><td class="value">$150k - $3.5MM</td></tr>
    <tr><td class="label">DTI</td><td class="value">50%; 55% up to 80% LTV and 680+ FICO for Primary and Second Home</td></tr>
    <tr><td class="label">FICO</td><td class="value">Lowest mid-FICO amongst all borrowers</td></tr>
    <tr><td class="label">Loan Purpose</td><td class="value">Purchase, Rate/Term, Cash Out</td></tr>
    <tr><td class="label">Max Cash Out</td><td class="value">$1,000,000</td></tr>
    <tr><td class="label">Occupancy</td><td class="value">Owner Occupied, Second Home, Investment</td></tr>
    <tr><td class="label">Prepay Penalty</td><td class="value">On investment properties as permitted by law</td></tr>
    <tr><td class="label">Eligible<br>Borrowers</td><td class="value">US Citizens<br>Permanent Resident Aliens Non-Permanent Resident Aliens Foreign Nationals (70 LTV max; 50% DTI max; Primary homes not permitted)</td></tr>
    <tr><td class="label">Rural</td><td class="value">Residential, non-agricultural up to 20 acres</td></tr>
    <tr><td class="label">FTHB</td><td class="value">Permitted (Investment property, IO not permitted)</td></tr>
    <tr><td class="label">Document Age</td><td class="value">Income, assets, title documents: 90 days Credit Report, Appraisal: 120 days</td></tr>
    <tr><td class="label">Ineligible States<br>&amp; Jurisdictions</td><td class="value">US Territories, Alaska, Hawaii, Michigan, Mississippi, Missouri, Nebraska, New Jersey, New York, North Carolina, North Dakota, Oklahoma, Pennsylvania, South Dakota, Vermont, West Virginia, Wyoming</td></tr>
  </table>

  <div class="section-tag" style="left:296px;top:330px;width:175px">Required Reserves*</div>
  <table class="spec-table" style="left:296px;top:365px;width:212px;height:82px">
    <colgroup><col style="width:46%"><col style="width:54%"></colgroup>
    <tr><td class="label" style="font-weight:400">$150,000 - $500,000</td><td class="value">3 Months</td></tr>
    <tr><td class="label" style="font-weight:400">$500,001 - $1.0MM</td><td class="value">6 Months</td></tr>
    <tr><td class="label" style="font-weight:400">$1.0MM - $2.0MM</td><td class="value">9 Months</td></tr>
    <tr><td class="label" style="font-weight:400">$2.0MM - $3.0MM</td><td class="value">12 Months</td></tr>
    <tr><td class="label" style="font-weight:400">&gt;$3.0MM</td><td class="value">18 Months</td></tr>
    <tr><td class="label" style="font-weight:400">Interest Only</td><td class="value">6 Months Minimum</td></tr>
  </table>
  <div class="note" style="left:304px;top:452px;width:200px">* &gt; 75 LTV with less than 12 months reserves subject to price adjustment.<br>See rate sheet for details.</div>

  <div class="section-tag" style="left:296px;top:500px;width:175px">Housing</div>
  <table class="spec-table" style="left:296px;top:534px;width:212px;height:46px">
    <colgroup><col style="width:30%"><col style="width:70%"></colgroup>
    <tr><td class="label">≥ 36 Months</td><td class="value">Loan amount &gt;$1.0MM, reduce max LTV 5%</td></tr>
    <tr><td class="label">≥ 24 Months</td><td class="value">All loan amounts reduce max LTV 5%</td></tr>
    <tr><td class="label">≥ 12 Months</td><td class="value">All loan amounts max LTV 70%</td></tr>
  </table>
  <ul class="bullet-notes" style="left:302px;top:592px;width:206px">
    <li>Bankruptcies require 12 month seasoning</li>
    <li>Chapter 7 seasoning based on discharge date to loan application date</li>
    <li>Chapter 13 seasoning based on discharged, dismissed, or completed date to loan application date</li>
    <li>DSCR transactions require 24 months seasoning</li>
    <li>Rolling mortgage lates graded as individual</li>
  </ul>

  <footer class="page-footer"><i>Effective November 1, 2024</i><span class="page-footer__rule"></span><span class="page-footer__num">1</span></footer>
</section>

<!-- ===================== PAGE 4 : SUMMIT SELECT MATRIX 2 ===================== -->
<section class="page page--light" style="left:606px;top:772px">
  <header class="matrix-header">
    <svg width="300" height="51" viewBox="0 0 300 51" aria-hidden="true"><polygon points="0,0 266,0 296,51 0,51" fill="#1b3619"/></svg>
    <div class="matrix-header__title">Summit Select</div>
    <div class="matrix-header__sub">Program Matrix</div>
  </header>

  <div class="section-tag" style="left:42px;top:71px;width:198px">Housing Information Cont.</div>

  <div class="table-title" style="left:53px;top:110px"><strong>Mortgage DQ Restrictions</strong></div>
  <table class="spec-table" style="left:42px;top:122px;width:219px;height:57px">
    <colgroup><col style="width:22%"><col style="width:78%"></colgroup>
    <tr><td class="label" style="font-weight:400">0x30x12</td><td class="value">No Adjustment</td></tr>
    <tr><td class="label" style="font-weight:400">1x30x12</td><td class="value">Loan amount &gt;$1.0MM, reduce max LTV 5%</td></tr>
    <tr><td class="label" style="font-weight:400">2x30x12</td><td class="value">All loan amounts reduce max LTV 5%</td></tr>
    <tr><td class="label" style="font-weight:400">0x60x12</td><td class="value">All loan amounts max LTV 70%</td></tr>
  </table>

  <div class="table-title" style="left:276px;top:110px"><strong>Property Types</strong></div>
  <table class="spec-table" style="left:271px;top:122px;width:241px;height:147px">
    <colgroup><col style="width:26%"><col style="width:74%"></colgroup>
    <tr><td class="label">Eligible:</td><td class="value">Single family, PUD, 2-4 unit, Warrantable Condo, Nonwarrantable Condo, Condotel, Modular, Ground Lease/ Lease Hold Properties, Rural properties, Historical Homes</td></tr>
    <tr><td class="label">Ineligible:</td><td class="value">Condo Conversion, Manufactured Home, Log Homes, Raw Land, Mixed-Use, Farms/Working Farms, Corporate Properties, Earth Homes, Burn Homes, Basement Homes, Environmental Conditions, Dwellings with &gt; 4 Units, Lagoons/Cesspools, Properties designated by the government as places of worship, Timeshares, Rooming/ Boarding Houses, Unique Properties, Properties &gt; 20 acres, Properties &lt; 600 sq. ft.</td></tr>
    <tr><td class="label">LTV<br>Restrictions:</td><td class="value">Non-warrantable Condo &amp; Condotel:<br>• Owner Occupied: 75 LTV Max<br>• Non-owner Occupied: 70 LTV Max</td></tr>
  </table>

  <div class="section-tag" style="left:42px;top:281px;width:198px">DSCR Program</div>
  <table class="spec-table" style="left:42px;top:317px;width:470px;height:356px">
    <colgroup><col style="width:16%"><col style="width:84%"></colgroup>
    <tr><td class="label">General<br>Requirements</td><td class="value">• Business purpose, investment properties only<br>• DSCR ≥ .75<br>• Must be exempt from ATR, QM, HPML requirements<br>• 1007 required<br>• 480 term term maximum; IO permitted<br>• Eligible property types: 1-4 Unit SFR, PUD, Co-op, Condotel, Warrantable and Non-Warrantable Condo<br>• 6 months reserves with 30-days bank statements<br>• FTHB <b>not permitted</b><br>• Minimum seasoning from housing event - 24 months<br>• Gift funds for down payment: 5% on LTV ≤ 80% or 10% on LTV &lt; 70%</td></tr>
    <tr><td class="label">Eligible Borrowers</td><td class="value">• US Citizens<br>• Permanent Resident Aliens<br>• Non-Permanent Resident Aliens<br>• Foreign Nationals who primarily live and work outside the US<br>• Limited Partnerships, General Partnerships, Corporations, Limited Liability Company - Personal Guarantor req'd.</td></tr>
    <tr><td class="label">Income Calculation</td><td class="value">Debt Service Coverage Ratio = Gross Income / Proposed PITIA*<br><b>Tenant Occupied:</b><br>&nbsp;&nbsp;• Use the lower of the executed lease agreement or the market rent from appraisal form 1007<br>&nbsp;&nbsp;&nbsp;- OR -<br>&nbsp;&nbsp;• Determined by fully executed lease in file with tenant currently occupying or will occupy within 30 days of the<br>&nbsp;&nbsp;&nbsp;Note date. Month-to-month lease also permitted<br><b>Non-Tenant Occupied:</b><br>&nbsp;&nbsp;• Market rent from appraisal form 1007 may be used solely<br>&nbsp;&nbsp;&nbsp;- OR -<br>&nbsp;&nbsp;• Short term rental income can be used (see below)<br><b>*Interest only:</b><br>For loans &lt; 5 years, DSCR is based on PITIA payment with principal and interest payments amortized over the scheduled remaining loan term. For loans ≥ 5 years, DSCR is based on interest only payments</td></tr>
    <tr><td class="label">Short Term Rentals<br>(STR)</td><td class="value">• Max loan size: $2.0MM<br>• Mortgage refinancing only (no purchase transactions)<br>• Minimum 12-month rental history<br>• DSCR calculated on average actual rental income over 12 months - no market rents are used in calculations<br>• 3rd party verification STR are legally permissible and licensed where applicable<br>• Rent loss coverage not required</td></tr>
  </table>

  <footer class="page-footer"><i>Effective November 1, 2024</i><span class="page-footer__rule"></span><span class="page-footer__num">2</span></footer>
</section>

<!-- ===================== PAGE 5 : KEYSTONE INVESTOR ===================== -->
<section class="page page--light" style="left:33px;top:1506px">
  <header class="matrix-header">
    <svg width="300" height="51" viewBox="0 0 300 51" aria-hidden="true"><polygon points="0,0 266,0 296,51 0,51" fill="#1b3619"/></svg>
    <div class="matrix-header__title">Keystone Investor</div>
    <div class="matrix-header__sub">Program Matrix</div>
  </header>

  <div class="table-title" style="left:43px;top:75px"><strong>DSCR 1.00+ &amp; Income Qualifying</strong></div>
  <table class="matrix" style="left:43px;top:90px;width:212px">
    <colgroup><col style="width:20%"><col style="width:20%"><col style="width:22%"><col style="width:19%"><col style="width:19%"></colgroup>
    <tr><th>FICO</th><th>Loan<br>Amount</th><th>Max LTV<br>Purchase</th><th>Max LTV<br>R/T</th><th>Max LTV<br>Cash Out</th></tr>
    <tr><td rowspan="4">700</td><td>≤$1.0MM</td><td>80</td><td>80</td><td>75</td></tr>
    <tr><td>$1.5MM</td><td>75</td><td>75</td><td>70</td></tr>
    <tr><td>$2.0MM</td><td>70</td><td>70</td><td>65</td></tr>
    <tr><td>$3.0MM</td><td>70</td><td>70</td><td>-</td></tr>
    <tr><td rowspan="4">699<br>-<br>660</td><td>≤$1.0MM</td><td>75</td><td>75</td><td>70</td></tr>
    <tr><td>$1.5MM</td><td>75</td><td>75</td><td>70</td></tr>
    <tr><td>$2.0MM</td><td>70</td><td>70</td><td>60</td></tr>
    <tr><td>$3.0MM</td><td>65</td><td class="na">-</td><td class="na">-</td></tr>
    <tr><td rowspan="4">659<br>-<br>620*</td><td>≤$1.0MM</td><td>70</td><td>70</td><td>65</td></tr>
    <tr><td>$1.5MM</td><td>65</td><td class="na">-</td><td class="na">-</td></tr>
    <tr><td>$2.0MM</td><td>65</td><td class="na">-</td><td class="na">-</td></tr>
    <tr><td>$3.0MM</td><td>60</td><td class="na">-</td><td class="na">-</td></tr>
  </table>
  <div class="note" style="left:212px;top:263px">*DSCR FICO ≥ 640</div>

  <div class="table-title" style="left:302px;top:75px"><strong>DSCR 1.00+ &amp; Income Qualifying</strong></div>
  <table class="matrix" style="left:302px;top:90px;width:212px">
    <colgroup><col style="width:20%"><col style="width:20%"><col style="width:22%"><col style="width:19%"><col style="width:19%"></colgroup>
    <tr><th>FICO</th><th>Loan<br>Amount</th><th>Max LTV<br>Purchase</th><th>Max LTV<br>R/T</th><th>Max LTV<br>Cash Out</th></tr>
    <tr><td rowspan="4">720</td><td>≤$1.0MM</td><td>75</td><td>75</td><td>70</td></tr>
    <tr><td>$1.5MM</td><td>70</td><td>70</td><td>65</td></tr>
    <tr><td>$2.0MM</td><td>65</td><td>65</td><td>60</td></tr>
    <tr><td>$3.0MM</td><td>65</td><td>65</td><td>-</td></tr>
    <tr><td rowspan="4">719<br>-<br>700</td><td>≤$1.0MM</td><td>70</td><td>70</td><td>65</td></tr>
    <tr><td>$1.5MM</td><td>70</td><td>70</td><td>65</td></tr>
    <tr><td>$2.0MM</td><td>65</td><td>65</td><td>60</td></tr>
    <tr><td>$3.0MM</td><td>60</td><td class="na">-</td><td class="na">-</td></tr>
    <tr><td rowspan="4">699<br>-<br>680</td><td>≤$1.0MM</td><td>70</td><td>70</td><td class="na">-</td></tr>
    <tr><td>$1.5MM</td><td>70</td><td class="na">70</td><td class="na">-</td></tr>
    <tr><td>$2.0MM</td><td>65</td><td class="na">65</td><td class="na">-</td></tr>
    <tr><td>$3.0MM</td><td>60</td><td class="na">-</td><td class="na">-</td></tr>
  </table>

  <div class="table-title plain" style="left:43px;top:282px"><strong>DSCR 1.00+</strong><br>Foreign National</div>
  <table class="matrix" style="left:43px;top:311px;width:212px">
    <colgroup><col style="width:20%"><col style="width:20%"><col style="width:22%"><col style="width:19%"><col style="width:19%"></colgroup>
    <tr><th>FICO</th><th>Loan<br>Amount</th><th>Max LTV<br>Purchase</th><th>Max LTV<br>R/T</th><th>Max LTV<br>Cash Out</th></tr>
    <tr><td rowspan="2" style="line-height:1.1">680<br>and<br>Foreign<br>Credit</td><td style="height:19px">≤$1.0MM</td><td>75</td><td>65</td><td>65</td></tr>
    <tr><td style="height:19px">$1.5MM</td><td>70</td><td>60</td><td>60</td></tr>
  </table>

  <div class="table-title plain" style="left:302px;top:282px"><strong>DSCR 0.75 - 0.99</strong><br>Foreign National</div>
  <table class="matrix" style="left:302px;top:311px;width:212px">
    <colgroup><col style="width:20%"><col style="width:20%"><col style="width:22%"><col style="width:19%"><col style="width:19%"></colgroup>
    <tr><th>FICO</th><th>Loan<br>Amount</th><th>Max LTV<br>Purchase</th><th>Max LTV<br>R/T</th><th>Max LTV<br>Cash Out</th></tr>
    <tr><td rowspan="2" style="line-height:1.1">680<br>and<br>Foreign<br>Credit</td><td style="height:19px">≤$1.0MM</td><td>65</td><td>60</td><td>60</td></tr>
    <tr><td style="height:19px">$1.5MM</td><td>60</td><td>-</td><td>-</td></tr>
  </table>

  <div class="section-tag" style="left:43px;top:392px;width:176px">General Requirements</div>
  <table class="spec-table" style="left:43px;top:427px;width:242px;height:105px">
    <colgroup><col style="width:26%"><col style="width:74%"></colgroup>
    <tr><td class="label">Product Type</td><td class="value">Fixed Rate: 30, 40-Yr (IO Only); 5/6 &amp; 7/6 ARM</td></tr>
    <tr><td class="label">Interest Only</td><td class="value">FICO 680+, Max 80% LTV (DSCR&lt; 1: Max 75% LTV)</td></tr>
    <tr><td class="label">Loan Amount</td><td class="value">$150k - $3.0MM</td></tr>
    <tr><td class="label">Loan Purpose</td><td class="value">Purchase, Rate/Term, Cash Out</td></tr>
    <tr><td class="label">Occupancy</td><td class="value">Non-Owner Occupied Business Purpose</td></tr>
    <tr><td class="label">Cash-in-Hand</td><td class="value">Currently free &amp; clear OR LTV&lt; 50%: Unlimited. LTV&gt;50% Max $1.0MM</td></tr>
    <tr><td class="label">Prepay Penalty</td><td class="value">As permitted by law</td></tr>
  </table>

  <div class="table-title" style="left:45px;top:551px"><strong>Max LTV by Property Type</strong></div>
  <table class="matrix" style="left:46px;top:565px;width:213px">
    <colgroup><col style="width:34%"><col style="width:22%"><col style="width:18%"><col style="width:26%"></colgroup>
    <tr><th>Property</th><th>Purchase</th><th>R/T</th><th>Cash Out</th></tr>
    <tr><td>Non-Warr. Condo</td><td>70</td><td>70</td><td>65</td></tr>
    <tr><td>Condo</td><td>80</td><td>80</td><td>70</td></tr>
    <tr><td>2-4 Unit DSCR &gt; 1</td><td>80</td><td>80</td><td>70</td></tr>
    <tr><td>Modular</td><td>80</td><td>80</td><td>70</td></tr>
  </table>

  <div class="section-tag" style="left:302px;top:392px;width:176px">Housing Information</div>
  <table class="matrix" style="left:302px;top:427px;width:212px">
    <colgroup><col style="width:23%"><col style="width:55%"><col style="width:22%"></colgroup>
    <tr><th>Event<br>Seasoning</th><th>Restrictions</th><th>Mortgage<br>DQ</th></tr>
    <tr><td>36 Months</td><td>No adjustment at any loan amount</td><td>1x30x12</td></tr>
    <tr><td>≥ 24 Months</td><td>Purchase 75% Max LTV; Refi 70% Max</td><td>2x30x12</td></tr>
    <tr><td>≥ 12 Months</td><td>Purchase 70% Max LTV; Refi 65% Max</td><td>0x60x12</td></tr>
  </table>
  <ul class="bullet-notes" style="left:305px;top:491px;width:209px">
    <li style="margin-bottom:1.5px">Chapter 7 seasoning based on discharge date</li>
    <li style="margin-bottom:1.5px">Chapter 13 seasoning based on filing date</li>
    <li style="margin-bottom:1.5px">DSCR transactions require 24 months seasoning from bankruptcy or housing events</li>
    <li style="margin-bottom:1.5px">Rolling mortgage lates graded as individual</li>
  </ul>

  <div class="section-tag" style="left:302px;top:568px;width:176px">Housing Information</div>
  <div class="plain-list" style="left:302px;top:602px;width:200px">
    <div><span style="width:83px">$150,000 - $500,000</span><span>3 Months</span></div>
    <div><span style="width:83px">$500,001 - $999,999</span><span>6 Months</span></div>
    <div><span style="width:83px">$1.0MM - $1.49MM</span><span>9 Months</span></div>
    <div><span style="width:83px">$1.5MM+</span><span>12 Months</span></div>
    <div><span style="width:83px">Interest Only</span><span>6 Months Minimum</span></div>
  </div>

  <footer class="page-footer"><i>Effective November 1, 2024</i><span class="page-footer__rule"></span><span class="page-footer__num">3</span></footer>
</section>

<!-- ===================== PAGE 6 : PORTFOLIO PRO ===================== -->
<section class="page page--light" style="left:606px;top:1506px">
  <header class="matrix-header">
    <svg width="300" height="51" viewBox="0 0 300 51" aria-hidden="true"><polygon points="0,0 266,0 296,51 0,51" fill="#1b3619"/></svg>
    <div class="matrix-header__title">Portfolio Pro</div>
    <div class="matrix-header__sub">Program Matrix</div>
  </header>
  <div class="note" style="right:41px;top:54px;font-style:normal;font-weight:600;font-size:5.2px">Requires one year of investment property ownership within the last three years</div>

  <div class="table-title plain" style="left:42px;top:89px"><strong>Non-Owner Business 5-8 Units</strong><br>DSCR 1.00+</div>
  <table class="matrix" style="left:42px;top:115px;width:219px">
    <colgroup><col style="width:22%"><col style="width:24%"><col style="width:18%"><col style="width:18%"><col style="width:18%"></colgroup>
    <tr><th>FICO</th><th>Loan<br>Amount</th><th>Max LTV<br>Purchase</th><th>Max LTV<br>R/T</th><th>Max LTV<br>Cash Out</th></tr>
    <tr><td rowspan="2">700</td><td style="height:19px">$400k - $1.5MM</td><td>75</td><td>70</td><td>65</td></tr>
    <tr><td style="height:19px">$1.5MM - $2.0MM</td><td>70</td><td>65</td><td>65</td></tr>
  </table>

  <div class="table-title plain" style="left:297px;top:89px"><strong>Non-Owner Business Cross-Collateralized Blanket</strong><br>DSCR 1.20+</div>
  <table class="matrix" style="left:297px;top:115px;width:211px">
    <colgroup><col style="width:20%"><col style="width:26%"><col style="width:18%"><col style="width:18%"><col style="width:18%"></colgroup>
    <tr><th>FICO</th><th>Loan<br>Amount</th><th>Max LTV<br>Purchase</th><th>Max LTV<br>R/T</th><th>Max LTV<br>Cash Out</th></tr>
    <tr><td style="height:15px">700</td><td>$400k - $3.0MM</td><td>70</td><td>65</td><td>65</td></tr>
    <tr><td style="height:24px;line-height:1.1">660 or<br>Foreign<br>National</td><td>$400k - $3.0MM</td><td>65</td><td>-</td><td>-</td></tr>
  </table>

  <div class="section-tag" style="left:42px;top:205px;width:176px">Required Reserves</div>
  <div class="plain-list" style="left:42px;top:240px;width:219px">
    <div><span style="width:83px">Loan amount ≤ $1.5MM</span><span>6 Months PITIA (ITIA-IO)</span></div>
    <div><span style="width:83px">Loan amount &gt; $1.5MM</span><span>9 Months PITIA (ITIA-IO)</span></div>
  </div>
  <ul class="bullet-notes" style="left:42px;top:264px;width:219px"><li>Cash out may not be used to satisfy requirement</li></ul>

  <div class="section-tag" style="left:297px;top:205px;width:176px">Required Reserves</div>
  <div class="plain-list" style="left:297px;top:240px;width:211px">
    <div><span style="width:83px">Loan amount ≤ $1.5MM</span><span>6 Months PITIA (ITIA-IO)</span></div>
    <div><span style="width:83px">Loan amount &gt; $1.5MM</span><span>9 Months PITIA (ITIA-IO)</span></div>
    <div><span style="width:83px">Loan amount &gt; $2.5MM</span><span>12 Months PITIA (ITIA-IO)</span></div>
  </div>
  <ul class="bullet-notes" style="left:297px;top:273px;width:211px"><li>Cash out may not be used to satisfy requirement</li></ul>

  <div class="section-tag" style="left:42px;top:309px;width:176px">General Requirements</div>
  <table class="spec-table" style="left:42px;top:344px;width:207px;height:231px">
    <colgroup><col style="width:35%"><col style="width:65%"></colgroup>
    <tr><td class="label">Product Type</td><td class="value">15, 30-Yr Fixed; 30-Yr IO<br>5, 7, 10-Yr ARM; 5, 7, 10-Yr ARM IO (30-Yr)</td></tr>
    <tr><td class="label">Interest Only</td><td class="value">Eligible</td></tr>
    <tr><td class="label">Loan Amount</td><td class="value">$400k - $2.0MM</td></tr>
    <tr><td class="label">Loan Purpose</td><td class="value">Purchase, Rate/Term, Cash Out</td></tr>
    <tr><td class="label">Occupancy</td><td class="value">Non-Owner Occupied Business Purpose</td></tr>
    <tr><td class="label">Property Type</td><td class="value">5-8 Units; 2-8 Mixed UseMax $1.0MM</td></tr>
    <tr><td class="label">Cash-in-Hand</td><td class="value">Limited to $1.0MM</td></tr>
    <tr><td class="label">Acreage/Rural</td><td class="value">Max 2 acres; rural ineligible</td></tr>
    <tr><td class="label">Prepay Penalty</td><td class="value">As permitted by law</td></tr>
    <tr><td class="label">DSCR Calculation*</td><td class="value">Monthly rent / proposed PITIA (ITIA for IO)</td></tr>
    <tr><td class="label">Experience</td><td class="value">One year of ownership within last three years</td></tr>
    <tr><td class="label">Lease Req.</td><td class="value">For all refinances on a month-to-month lease, a current lease must be provided and supported with two most recent bank statements showing consecutive rental payments</td></tr>
  </table>
  <div class="note" style="left:42px;top:586px;font-style:normal">*Reduce qualifying rents by any management fee reflected<br>on the appraisal report</div>

  <div class="section-tag" style="left:297px;top:309px;width:176px">General Requirements</div>
  <table class="spec-table" style="left:297px;top:344px;width:207px;height:314px">
    <colgroup><col style="width:33%"><col style="width:67%"></colgroup>
    <tr><td class="label">Product Type</td><td class="value">15, 30-Yr Fixed; 30-Yr IO<br>5, 7, 10-Yr ARM; 5, 7, 10-Yr ARM IO (30-Yr)</td></tr>
    <tr><td class="label">Interest Only</td><td class="value">Eligible</td></tr>
    <tr><td class="label">Loan Amount</td><td class="value">$400k - $3.0MM</td></tr>
    <tr><td class="label">Loan Purpose</td><td class="value">Purchase, Rate/Term, Cash Out</td></tr>
    <tr><td class="label">Occupancy</td><td class="value">Non-Owner Occupied Business Purpose</td></tr>
    <tr><td class="label">Property Type</td><td class="value">1-4 Units, including Condos</td></tr>
    <tr><td class="label">DSCR<br>Calculations</td><td class="value">Property &amp; loan DSCR both require 1.20+ calculated as follows:<br>Loan DSCR: Total gross rental income for all properties/loan PITIA (ITIA-IO) Property DSCR: Rental income per property/allocated loan amount PITIA (ITIA-IO) Both IO and regular AM payments require a DSCR of 1.20+</td></tr>
    <tr><td class="label">Property Count</td><td class="value">3 to 25 properties with $50k minimum property allocation; $1.0MM max allocation</td></tr>
    <tr><td class="label">Cash-in-Hand</td><td class="value">Unlimited when LTV ≤ 65</td></tr>
    <tr><td class="label">Acreage/Rural</td><td class="value">Max 2 acres; rural ineligible</td></tr>
    <tr><td class="label">Prepay Penalty</td><td class="value">As permitted by law</td></tr>
    <tr><td class="label">Experience</td><td class="value">One year of ownership within last three years</td></tr>
    <tr><td class="label">Lease Req.</td><td class="value">For all refinances on a month-to-month lease, a current lease must be provided and supported with two most recent bank statements showing consecutive rental payments</td></tr>
  </table>

  <footer class="page-footer"><i>Effective November 1, 2024</i><span class="page-footer__rule"></span><span class="page-footer__num">4</span></footer>
</section>

</body>
</html>
```